Need a Wordpress website for my HVAC company

I need a Wordpress website created for an HVAC company in a competitive market.
Following are some websites I like:
My current website is www.brovikclimate.com - we also have a facebook page with some pictures

We are an airconditioning and heating company that does both residential and commmercial work.
We need the following info on our website:
-mobile friendly
-Schedule an appt -repair/maintnenace/installation (i would like this option to always be on the page even if they scroll down.)
-24 hour service
-coupons /promotions
-financing
-reviews/testimonials
-about
-blog
-Our service area
The following are services we provide:
-Air conditioning - Installation/Service/Maintenance/new construction
-Heating - Installation/Service/Maintenance/new construction ( gas furnace, 2 stage furnace, electric heat)
-Duct - Repair/Replacement/Istallation - (zone systems)
-thermostats (wifi)
-Heat pump
-Air handler
-self communicating systems
-carbon monoxide testing
-hail damage
-duct sealing
-insulation
-Air cleaners - UV Air purifiers
-humidifiers

I would also like Quillo SEO add on

Target Market(s)

Anyone who needs our services HVAC contractor

Industry/Entity Type

Hvac

Contact Information for Business Card

Phone:480-555-2064
website:www.brovikclimate.com
email pmarsh@brovikclimate.com

Coding

Coded - Design and coding required

Number of Pages Required

5+ page

Font styles to use
Serif
Sans Serif

Requirements
Must have
• I wrote in brief. I already have Nimbo Vault. Long story I paid for 3 years already. I need someone to put website there. Ive never used Wordpress but would like a template page so I can easily add services.
Nice to have
• Clean, bright, original

```html
<!DOCTYPE html>
<html lang="en">
<head>
<meta charset="utf-8">
<title>Brovik Climate Services — Heating &amp; Cooling</title>
<link href="https://fonts.googleapis.com/css2?family=Open+Sans:ital,wght@0,300;0,400;0,600;0,700;1,400&display=swap" rel="stylesheet">
<style>
:root{
  --blue:#1f62a8;
  --blue-dark:#0f4a8a;
  --green:#1f9147;
  --green-dark:#177a3a;
  --red:#d42a35;
  --red-dark:#b61f2a;
  --ink:#3a3a3a;
  --muted:#8a8a8a;
  --heading-red:#c8262f;
  --footer:#e6e6e6;
  --white:#ffffff;
}
*{box-sizing:border-box;margin:0;padding:0}
html,body{width:1200px;height:3015px;overflow:hidden}
body{font-family:"Open Sans",Arial,sans-serif;color:var(--ink);background:var(--white);position:relative}

/* header */
.site-header{position:absolute;left:0;top:0;width:1200px;height:118px;background:var(--white)}
.brand{position:absolute;left:132px;top:30px;display:flex;align-items:center;gap:12px}
.brand-dot{width:40px;height:40px;border-radius:50%;background:var(--red)}
.brand-name{font-size:28px;font-weight:700;color:var(--blue-dark);line-height:1}
.call{position:absolute;right:158px;top:46px;text-align:right}
.call-label{font-size:17px;color:var(--green)}
.call-number{font-size:21px;color:#333;display:flex;align-items:center;gap:8px;margin-top:4px}
.phone-icon{width:22px;height:22px;border-radius:4px;background:var(--green);display:inline-flex;align-items:center;justify-content:center}

/* nav */
.main-nav{position:absolute;left:0;top:118px;width:1200px;height:58px;background:linear-gradient(#2a71b8,#114e91)}
.main-nav ul{list-style:none;display:flex;position:absolute;left:142px;top:0;height:58px;align-items:center}
.main-nav li{font-size:17px;font-weight:600;color:var(--white);padding:0 18px;height:58px;display:flex;align-items:center;border-right:1px solid rgba(255,255,255,.18)}
.main-nav li:last-child{border-right:none}
.main-nav li.active{position:relative}
.main-nav li.active::before{content:"";position:absolute;left:2px;right:2px;top:10px;bottom:10px;border-radius:10px;background:rgba(255,255,255,.18);border:1px solid rgba(255,255,255,.35)}
.main-nav li.active span{position:relative}

/* hero */
.hero{position:absolute;left:0;top:176px;width:1200px;height:472px;
  background:
    radial-gradient(ellipse 160px 90px at 760px 60px,rgba(226,190,60,.55),rgba(226,190,60,0)),
    radial-gradient(ellipse 300px 260px at 900px 260px,rgba(70,110,160,.75),rgba(70,110,160,0)),
    radial-gradient(ellipse 260px 180px at 540px 300px,rgba(150,60,50,.35),rgba(150,60,50,0)),
    linear-gradient(100deg,#6f7478 0%,#a3a8ab 22%,#c4c2bb 40%,#8e8f8c 55%,#6a7f96 75%,#4b6b8f 100%)}
.hero-title{position:absolute;left:0;width:1180px;top:148px;text-align:center;color:var(--white);font-size:46px;font-weight:600;line-height:50px;letter-spacing:1px;text-shadow:0 2px 6px rgba(0,0,0,.35)}
.hero-dots{position:absolute;left:1034px;top:196px;display:flex;flex-direction:column;gap:6px}
.hero-dots span{width:14px;height:14px;border-radius:50%;background:rgba(255,255,255,.6)}
.hero-dots span:first-child{background:var(--white)}

/* appointment cards */
.appt{position:absolute;top:618px;width:302px;height:212px;text-align:center;color:var(--white)}
.appt-hex{position:absolute;left:91px;top:-64px;width:120px;height:130px}
.appt-kicker{position:absolute;left:0;right:0;top:90px;font-size:16px;font-weight:600;letter-spacing:.2px}
.appt-type{position:absolute;left:0;right:0;top:116px;font-size:23px;font-weight:600;letter-spacing:.5px}
.appt-btn{position:absolute;left:90px;top:160px;width:122px;height:32px;line-height:32px;font-size:13px;font-weight:700;border-radius:2px}
.appt.repair{left:147px;background:var(--green)}
.appt.repair .appt-btn{background:var(--green-dark)}
.appt.maintenance{left:449px;background:var(--red)}
.appt.maintenance .appt-btn{background:var(--red-dark)}
.appt.installation{left:751px;background:var(--blue)}
.appt.installation .appt-btn{background:#2a7ccc}

/* why choose us */
.section-title{position:absolute;left:0;width:1200px;text-align:center;font-size:30px;font-weight:400;letter-spacing:.5px}
.why-title{top:878px;color:var(--heading-red)}
.why-text{position:absolute;left:175px;width:850px;top:926px;text-align:center;font-size:14.5px;line-height:23px;color:var(--muted)}
.video{position:absolute;left:138px;top:1048px;width:412px;height:248px;
  background:
    radial-gradient(ellipse 50px 50px at 100px 115px,rgba(220,110,40,.6),rgba(220,110,40,0)),
    radial-gradient(ellipse 90px 110px at 310px 110px,rgba(20,22,24,.85),rgba(20,22,24,0)),
    linear-gradient(90deg,#d9dbdc 0%,#b9bdbf 30%,#8d9296 55%,#4a4f53 75%,#2b2e31 100%)}
.play{position:absolute;left:182px;top:101px;width:46px;height:46px;border-radius:50%;background:var(--white);display:flex;align-items:center;justify-content:center}
.feature{position:absolute;width:230px}
.feature svg{position:absolute;left:0;top:2px}
.feature-name{margin-left:42px;font-size:15.5px;line-height:20px;color:#333}
.feature-desc{margin-left:42px;margin-top:8px;font-size:11px;line-height:15px;color:var(--muted)}

/* services */
.services{position:absolute;left:0;top:1380px;width:1200px;height:355px;background:linear-gradient(90deg,rgba(31,145,71,.94),rgba(31,145,71,.88)),linear-gradient(90deg,#6ea57f,#3d8f5a)}
.services-notch{position:absolute;left:578px;top:0;width:0;height:0;border-left:22px solid transparent;border-right:22px solid transparent;border-top:22px solid var(--white)}
.services-title{top:50px;color:var(--white);font-size:27px}
.services-lines{position:absolute;left:0;width:1200px;top:100px;text-align:center;color:var(--white);font-size:15px;line-height:26px}
.services-col{position:absolute;list-style:none;color:var(--white);font-size:14.5px;line-height:26px}
.services-col li::before,.finance-list li::before{content:"";display:inline-block;width:0;height:0;border-top:5px solid transparent;border-bottom:5px solid transparent;border-left:6px solid currentColor;margin-right:10px;vertical-align:1px}

/* testimonial */
.testimonial{position:absolute;left:0;top:1735px;width:1200px;height:395px;background:linear-gradient(90deg,rgba(24,96,170,.93),rgba(24,96,170,.88)),linear-gradient(90deg,#7aa2c9,#2f6aa8)}
.testimonial-title{top:52px;color:var(--white);font-size:26px}
.quote-box{position:absolute;left:292px;top:120px;width:601px;height:185px;background:var(--white);border-radius:3px}
.quote-box::after{content:"";position:absolute;left:278px;bottom:-20px;border-left:22px solid transparent;border-right:22px solid transparent;border-top:20px solid var(--white)}
.quote-text{position:absolute;left:60px;right:60px;top:32px;text-align:center;font-style:italic;font-size:15px;line-height:27px;color:#555}
.quote-mark{position:absolute;top:24px;font-size:56px;line-height:40px;color:#1f4f86;font-family:Georgia,serif;font-weight:700}
.quote-author{position:absolute;left:0;width:1200px;top:340px;text-align:center;color:var(--white);font-size:14px;font-weight:600;letter-spacing:.4px}

/* financing */
.finance-title{top:2172px;color:var(--heading-red);font-size:27px}
.finance-photo{position:absolute;left:150px;top:2202px;width:300px;height:310px}
.finance-intro{position:absolute;left:580px;top:2246px;width:440px;font-size:15.5px;line-height:23px;color:#444}
.finance-list{position:absolute;left:580px;top:2310px;list-style:none;font-size:13px;line-height:29px;color:#444}
.finance-list li::before{color:var(--green)}
.van{position:absolute;left:315px;top:2500px;width:530px;height:190px;z-index:2;border-radius:24px 40px 14px 14px;
  background:
    radial-gradient(ellipse 140px 80px at 300px 95px,rgba(255,255,255,.55),rgba(255,255,255,0)),
    linear-gradient(90deg,#dfe4ea 0%,#c9d3de 25%,#2e6db3 45%,#3b7cc4 75%,#d8dee6 100%)}

/* footer */
.site-footer{position:absolute;left:0;top:2670px;width:1200px;height:345px;background:var(--footer)}
.footer-mascot{position:absolute;left:145px;top:50px;width:70px;height:150px;background:linear-gradient(#d8c2a8 0%,#d8c2a8 20%,#3e6fae 20%,#23508a 100%);border-radius:6px}
.footer-brand{position:absolute;left:226px;top:108px;font-size:19px;font-weight:700;color:var(--blue-dark);line-height:22px}
.footer-col{position:absolute;top:72px}
.footer-col h4{font-size:15px;font-weight:600;color:#1d3f72;letter-spacing:.5px;margin-bottom:12px}
.footer-col ul{list-style:none;font-size:13px;line-height:30px;color:#777}
.socials{display:flex;gap:10px;margin-top:10px}
.socials span{width:32px;height:32px;border-radius:50%;background:var(--white);border:1px solid #cfcfcf}
.footer-rule{position:absolute;left:142px;top:280px;width:916px;height:1px;background:#cfcfcf}
.copyright{position:absolute;left:0;width:1200px;top:300px;text-align:center;font-size:11px;color:#999}
</style>
</head>
<body>

<header class="site-header">
  <div class="brand">
    <span class="brand-dot"></span>
    <span class="brand-name">Brovik Climate</span>
  </div>
  <div class="call">
    <div class="call-label">Call Us Now</div>
    <div class="call-number">
      <span class="phone-icon"><svg width="14" height="14" viewBox="0 0 24 24"><path fill="#fff" d="M6.6 10.8a15 15 0 0 0 6.6 6.6l2.2-2.2c.3-.3.7-.4 1-.2 1.1.4 2.3.6 3.6.6.6 0 1 .4 1 1V20c0 .6-.4 1-1 1A17 17 0 0 1 3 4c0-.6.4-1 1-1h3.5c.6 0 1 .4 1 1 0 1.3.2 2.5.6 3.6.1.3 0 .7-.2 1z"/></svg></span>
      (480-555-2064)
    </div>
  </div>
</header>

<nav class="main-nav">
  <ul>
    <li class="active"><span>Home</span></li>
    <li>About us</li>
    <li>24 hour Services</li>
    <li>Coupons</li>
    <li>Financing</li>
    <li>Reviews</li>
    <li>Blog</li>
    <li>Contact us</li>
  </ul>
</nav>

<section class="hero" role="img" aria-label="Technician in a hard hat repairing an outdoor air conditioning unit">
  <h1 class="hero-title">AIR CONDITIONING<br>AND HEATING REPAIRING</h1>
  <div class="hero-dots"><span></span><span></span><span></span></div>
</section>

<div class="appt repair">
  <svg class="appt-hex" viewBox="0 0 120 130"><polygon points="60,3 115,34 115,96 60,127 5,96 5,34" fill="#1f9147" stroke="#fff" stroke-width="3"/><g stroke="#fff" stroke-width="6" stroke-linecap="round"><line x1="42" y1="47" x2="78" y2="83"/><line x1="78" y1="47" x2="42" y2="83"/></g><circle cx="42" cy="47" r="8" fill="none" stroke="#fff" stroke-width="4"/></svg>
  <div class="appt-kicker">SCHEDULE AN APPOINTMENT</div>
  <div class="appt-type">REPAIR</div>
  <div class="appt-btn">CLICK HERE</div>
</div>
<div class="appt maintenance">
  <svg class="appt-hex" viewBox="0 0 120 130"><polygon points="60,3 115,34 115,96 60,127 5,96 5,34" fill="#d42a35" stroke="#fff" stroke-width="3"/><circle cx="60" cy="65" r="20" fill="none" stroke="#fff" stroke-width="8" stroke-dasharray="7 4"/><circle cx="60" cy="65" r="8" fill="#fff"/><line x1="66" y1="71" x2="84" y2="89" stroke="#fff" stroke-width="6" stroke-linecap="round"/></svg>
  <div class="appt-kicker">SCHEDULE AN APPOINTMENT</div>
  <div class="appt-type">MAINTENANCE</div>
  <div class="appt-btn">CLICK HERE</div>
</div>
<div class="appt installation">
  <svg class="appt-hex" viewBox="0 0 120 130"><polygon points="60,3 115,34 115,96 60,127 5,96 5,34" fill="#1f62a8" stroke="#fff" stroke-width="3"/><rect x="34" y="46" width="52" height="40" rx="4" fill="none" stroke="#fff" stroke-width="4"/><line x1="34" y1="56" x2="86" y2="56" stroke="#fff" stroke-width="3"/><circle cx="60" cy="72" r="8" fill="none" stroke="#fff" stroke-width="3"/></svg>
  <div class="appt-kicker">SCHEDULE AN APPOINTMENT</div>
  <div class="appt-type">INSTALLATION</div>
  <div class="appt-btn">CLICK HERE</div>
</div>

<h2 class="section-title why-title">WHY CHOOSE US</h2>
<p class="why-text">Brovik Climate Services is the premier residential heating, air conditioning, and energy solutions provider in the greater Phoenix area. We can help you lower your energy bills, reduce your environmental impact, and increase the comfort of your home. We design, install, service, repair and maintain residential air conditioning</p>

<div class="video" role="img" aria-label="Video still of a technician servicing a rooftop air conditioning unit">
  <div class="play"><svg width="18" height="20" viewBox="0 0 18 20"><polygon points="2,0 18,10 2,20" fill="#222"/></svg></div>
</div>

<div class="feature" style="left:570px;top:1045px">
  <svg width="30" height="30" viewBox="0 0 30 30"><circle cx="15" cy="15" r="12" fill="none" stroke="#1f4f86" stroke-width="3"/><path d="M15 8v7h6" fill="none" stroke="#1f4f86" stroke-width="3"/></svg>
  <div class="feature-name">Same Day<br>Service</div>
  <div class="feature-desc">You need air conditioning service when you need it, not when we feel like being open. Call now.</div>
</div>
<div class="feature" style="left:805px;top:1045px">
  <svg width="30" height="30" viewBox="0 0 30 30"><polygon points="15,3 24,25 6,25" fill="#1f4f86"/><rect x="3" y="25" width="24" height="3" fill="#1f4f86"/><rect x="9" y="13" width="12" height="3" fill="#fff"/></svg>
  <div class="feature-name">24/7 Emergency<br>Service</div>
  <div class="feature-desc">You deserve a fast solution to your problem. We provide it - right away.</div>
</div>
<div class="feature" style="left:570px;top:1170px">
  <svg width="30" height="30" viewBox="0 0 30 30"><line x1="6" y1="25" x2="19" y2="12" stroke="#1f4f86" stroke-width="4" stroke-linecap="round"/><circle cx="21" cy="9" r="6" fill="none" stroke="#1f4f86" stroke-width="3"/></svg>
  <div class="feature-name">Highly Trained<br>Technicians</div>
  <div class="feature-desc">It will install or repair your brand air conditioning and heating system for top reliability, energy savings, and property value.</div>
</div>
<div class="feature" style="left:805px;top:1170px">
  <svg width="30" height="30" viewBox="0 0 30 30"><rect x="8" y="8" width="14" height="11" rx="2" fill="#1f4f86"/><rect x="10" y="2" width="3" height="7" fill="#1f4f86"/><rect x="17" y="2" width="3" height="7" fill="#1f4f86"/><path d="M15 19v5q0 3-4 3" fill="none" stroke="#1f4f86" stroke-width="3"/></svg>
  <div class="feature-name">Free Energy<br>Survey</div>
  <div class="feature-desc">for replacement air conditioning and heating systems. Let us help you get maximum comfort and savings. No obligation.</div>
</div>

<section class="services">
  <div class="services-notch"></div>
  <h2 class="section-title services-title">OUR SERVICES</h2>
  <div class="services-lines">
    Air conditioning - Installation/Service/Maintenance/new construction<br>
    Heating - Installation/Service/Maintenance/new construction ( gas furnace, 2 stage furnace, electric heat)<br>
    Duct - Repair/Replacement/Istallation - (zone systems)
  </div>
  <ul class="services-col" style="left:372px;top:205px">
    <li>Thermostats (wifi)</li>
    <li style="margin-left:18px">Heat pump</li>
    <li style="margin-left:18px">Air handler</li>
  </ul>
  <ul class="services-col" style="left:630px;top:205px">
    <li>Self communicating systems</li>
    <li>Carbon monoxide testing</li>
    <li style="margin-left:48px">Hail damage</li>
  </ul>
</section>

<section class="testimonial">
  <h2 class="section-title testimonial-title">WHAT OUR CLIENT SAYS</h2>
  <div class="quote-box">
    <span class="quote-mark" style="left:24px">&ldquo;</span>
    <span class="quote-mark" style="right:24px">&rdquo;</span>
    <p class="quote-text">The Service I recieved from Brovik Climate was wonderful. My Expeirence throughtout the entire process was amazing, From the first call to service technician that came to my home, the service and the price, I was amazed and 100% satisfied.</p>
  </div>
  <div class="quote-author">DARA K. SCOTTSDALE, AZ</div>
</section>

<h2 class="section-title finance-title">NEED FINANCING?</h2>
<svg class="finance-photo" viewBox="0 0 300 310" role="img" aria-label="Technician in a hard hat working on an outdoor condenser unit">
  <defs>
    <linearGradient id="photoTone" x1="0" y1="0" x2="1" y2="1">
      <stop offset="0" stop-color="#c9ccce"/>
      <stop offset=".35" stop-color="#b3b0a6"/>
      <stop offset=".65" stop-color="#6f8aa8"/>
      <stop offset="1" stop-color="#2f5583"/>
    </linearGradient>
    <radialGradient id="hatTone" cx=".62" cy=".22" r=".22">
      <stop offset="0" stop-color="#e6c24a" stop-opacity=".7"/>
      <stop offset="1" stop-color="#e6c24a" stop-opacity="0"/>
    </radialGradient>
  </defs>
  <path d="M148 12 L286 12 L286 158 A138 140 0 1 1 148 12 Z" fill="#f2f2f2" stroke="#dadada" stroke-width="2"/>
  <path d="M148 24 L274 24 L274 158 A126 128 0 1 1 148 24 Z" fill="url(#photoTone)"/>
  <path d="M148 24 L274 24 L274 158 A126 128 0 1 1 148 24 Z" fill="url(#hatTone)"/>
</svg>
<p class="finance-intro">Brovik Climate Services offers many different financing plans. The top reasons to finance with us are:</p>
<ul class="finance-list">
  <li><span style="color:#444">Low cost same as cash financing for qualifying customers.</span></li>
  <li><span style="color:#444">Fast and easy application.</span></li>
  <li><span style="color:#444">Fast credit decisions.</span></li>
  <li><span style="color:#444">Monthly payments as low as $56.90 per month.</span></li>
  <li><span style="color:#444">No lien on your home</span></li>
</ul>
<div class="van" role="img" aria-label="Photo of the company service van with branded wrap"></div>

<footer class="site-footer">
  <div class="footer-mascot" role="img" aria-label="Mascot technician giving a thumbs up"></div>
  <div class="footer-brand">Brovik<br>Climate</div>
  <div class="footer-col" style="left:392px">
    <h4>INFORMATION</h4>
    <ul><li>Home</li><li>About Us</li><li>Why Choose Us</li><li>Videos</li></ul>
  </div>
  <div class="footer-col" style="left:567px">
    <h4>RESOURCES</h4>
    <ul><li>Order Food</li><li>Testimonials</li><li>Contact Us</li><li>My Account</li></ul>
  </div>
  <div class="footer-col" style="left:737px">
    <h4>SUPPORT</h4>
    <ul><li>Order Food</li><li>Testimonials</li><li>Contact Us</li><li>My Account</li></ul>
  </div>
  <div class="footer-col" style="left:884px">
    <h4>FOLLOW US</h4>
    <div class="socials"><span></span><span></span><span></span><span></span></div>
  </div>
  <div class="footer-rule"></div>
  <div class="copyright">© 2016 Company Name &nbsp;All right reserved &nbsp;Term of Use</div>
</footer>

</body>
</html>
```